Covid19 Poster for workplaces

Create a poster on how to protect yourself from Corona virus at work.
We are a Teamsafe Care company. We have just re-branded so we need to fit in with our brand. We like clean and fresh, slightly amusing is ok if it will draw attention but it's an important topic. A4 and A3 please.

Content:

Headline: Lower the risk of COVID 19 in the workplace.

BE WELL

Bring your own cup - don’t share cups and food.
Elbow tap instead of handshakes and kisses
Wash your hands often - with soap.
Elbow or tissues when you cough or sneeze then straight in the bin
Leave your face alone after touching shared surfaces
Leave your bugs at home if you’re feeling unwell.

Call health line if you have a cough, a high temperature and shortness of breath. 0800 472 9160

Based on recommendations from IPB and DCT

Target Market(s)

Employees - so anyone

Other font styles liked:
• Use the closest font to the brand documents

Requirements
Should not have
• Clip art

```html
<!DOCTYPE html>
<html lang="en">
<head>
<meta charset="utf-8">
<title>Lower the risk of COVID 19 in the workplace</title>
<link rel="stylesheet" href="https://fonts.googleapis.com/css2?family=Fira+Sans+Extra+Condensed:wght@300;400;700;800&family=Montserrat:wght@700&display=swap">
<style>
  :root {
    --navy: #2e3a8c;
    --teal: #1bafb8;
    --green: #8dc63f;
    --pink: #f6a09d;
    --blush: #fcf1ee;
    --white: #ffffff;
    --ink: #231f20;
    --rule: #e5d13a;
  }
  * { margin: 0; padding: 0; box-sizing: border-box; }
  html, body { width: 849px; height: 1200px; overflow: hidden; }
  body {
    position: relative;
    background: var(--white);
    font-family: "Fira Sans Extra Condensed", "Arial Narrow", sans-serif;
    color: var(--white);
  }
  .poster { position: absolute; inset: 0; }

  .backdrop {
    position: absolute; left: 0; top: 242px; width: 849px; height: 820px;
    background: radial-gradient(ellipse at 70% 30%, #fdf6f4 0%, var(--blush) 55%, #f6ecea 100%);
  }
  .stripe-teal { position: absolute; left: 10px; top: 242px; width: 33px; height: 958px; background: var(--teal); }
  .stripe-pink { position: absolute; left: 105px; top: 242px; width: 153px; height: 958px; background: var(--pink); }

  .brand {
    position: absolute; left: 0; top: 0; width: 258px; height: 242px;
    display: flex; align-items: center; justify-content: center; gap: 10px;
    background: var(--white);
  }
  .brand-dot { width: 22px; height: 22px; border-radius: 50%; background: var(--teal); }
  .brand-name {
    font-family: "Montserrat", sans-serif; font-weight: 700; font-size: 26px;
    line-height: 1.05; color: var(--ink);
  }

  .hero {
    position: absolute; left: 258px; top: 0; width: 591px; height: 242px;
    background: radial-gradient(circle at 80% 40%, #1d5fa8 0%, #1b5aa4 35%, #134a8e 70%, #0f3c7a 100%);
  }
  .hero-rule { position: absolute; left: 0; top: 201px; width: 591px; height: 1px; background: var(--rule); }
  .headline {
    position: absolute; left: 0; top: 14px; width: 591px; text-align: center;
    font-weight: 700; text-transform: uppercase; line-height: 1;
  }
  .headline .line-sm { display: block; font-size: 56px; letter-spacing: 0.5px; }
  .headline .line-lg { display: block; font-size: 82px; margin: 6px 0 4px; }

  .section-band {
    position: absolute; left: 0; top: 267px; width: 809px; height: 51px;
    background: var(--teal);
    clip-path: polygon(0 0, 765px 0, 809px 51px, 0 51px);
  }
  .section-title {
    position: absolute; left: 297px; top: 270px; font-size: 40px; line-height: 44px;
    font-weight: 300; letter-spacing: -0.5px;
  }
  .section-title strong { font-weight: 700; }

  .tip {
    position: absolute; left: 279px; width: 570px;
    display: flex; align-items: center; padding-left: 21px;
    font-size: 25px; font-weight: 300; line-height: 36px; letter-spacing: -0.3px;
  }
  .tip strong { font-weight: 700; letter-spacing: -0.6px; }
  .tip--navy { background: var(--navy); }
  .tip--green { background: var(--green); }
  .tip--pink { background: var(--pink); }
  .tip--teal { background: var(--teal); }

  .icon { position: absolute; left: 140px; width: 90px; height: 80px; }

  .footer-call {
    position: absolute; left: 0; top: 1062px; width: 554px; height: 90px;
    background: var(--navy);
    clip-path: polygon(0 0, 554px 0, 493px 90px, 0 90px);
  }
  .footer-source {
    position: absolute; left: 493px; top: 1062px; width: 356px; height: 90px;
    background: var(--teal);
    clip-path: polygon(61px 0, 356px 0, 356px 90px, 0 90px);
  }
  .call-text {
    position: absolute; left: 30px; top: 1071px; font-size: 26px; line-height: 36px;
    font-weight: 300; letter-spacing: -0.4px;
  }
  .call-text strong { font-weight: 700; font-size: 28px; }
  .source-text {
    position: absolute; right: 40px; top: 1071px; text-align: right;
    font-size: 26px; line-height: 36px; font-weight: 300; letter-spacing: -0.4px;
  }
  .source-text strong { font-weight: 700; }
</style>
</head>
<body>
<main class="poster">
  <div class="backdrop" role="img" aria-label="Soft pale pink background with faint virus particles"></div>
  <div class="stripe-teal"></div>
  <div class="stripe-pink"></div>

  <header>
    <div class="brand">
      <span class="brand-dot"></span>
      <span class="brand-name">Teamsafe<br>Care</span>
    </div>
    <div class="hero" role="img" aria-label="Blue close-up of coronavirus particles">
      <div class="hero-rule"></div>
      <h1 class="headline">
        <span class="line-sm">Lower the risk of</span>
        <span class="line-lg">COVID 19</span>
        <span class="line-sm">in the workplace</span>
      </h1>
    </div>
  </header>

  <div class="section-band"></div>
  <h2 class="section-title">BE <strong>WELL</strong></h2>

  <svg class="icon" style="top:340px" viewBox="0 0 90 80" aria-label="Cup icon">
    <g fill="none" stroke="#fff" stroke-width="2" stroke-linecap="round">
      <path d="M26 4 q-3 4 0 8 q3 4 0 8"/><path d="M35 4 q-3 4 0 8 q3 4 0 8"/><path d="M44 4 q-3 4 0 8 q3 4 0 8"/>
    </g>
    <path d="M16 28 h44 v18 q0 20 -20 20 h-4 q-20 0 -20 -20z" fill="#fff"/>
    <circle cx="62" cy="40" r="9" fill="none" stroke="#fff" stroke-width="5"/>
    <path d="M4 72 h68 q-4 6 -10 6 h-48 q-6 0 -10 -6z" fill="#fff"/>
  </svg>

  <svg class="icon" style="top:455px" viewBox="0 0 90 80" role="img" aria-label="Icon of two elbows tapping">
    <path d="M30 44 l18 -16 l32 10 l-10 16 l-20 -2 l4 20z" fill="#fff"/>
    <path d="M8 16 l8 8 l4 -12 l6 10 l8 -10 l2 12" fill="none" stroke="#fff" stroke-width="3"/>
  </svg>

  <svg class="icon" style="top:560px" viewBox="0 0 90 80" role="img" aria-label="Icon of hands being washed">
    <path d="M8 50 q0 -20 20 -24 l22 -12 l4 6 l-10 10 h30 v8 h-24 v8 h28 v8 h-28 v8 h20 v8 h-40 q-22 0 -22 -20z" fill="#fff"/>
  </svg>

  <svg class="icon" style="top:678px" viewBox="0 0 90 80" role="img" aria-label="Icon of a person coughing">
    <path d="M20 4 h28 v70 h-28z" fill="#fff" rx="10"/>
    <circle cx="72" cy="52" r="10" fill="none" stroke="#fff" stroke-width="4"/>
  </svg>

  <svg class="icon" style="top:818px" viewBox="0 0 90 80" role="img" aria-label="Icon of a finger touching a surface">
    <path d="M34 14 v32 l-8 -6 q-8 -2 -6 8 l16 30 h26 l6 -20 v-24 h-24 v-20z" fill="#fff"/>
    <path d="M37 2 v6 M24 8 l4 4 M50 8 l-4 4" stroke="#fff" stroke-width="3" stroke-linecap="round"/>
  </svg>

  <svg class="icon" style="top:950px;height:76px" viewBox="0 0 90 80" aria-label="Home icon">
    <path d="M6 38 l38 -34 l38 34" fill="none" stroke="#fff" stroke-width="6"/>
    <path d="M18 40 l26 -22 l26 22 v38 h-18 v-18 h-16 v18 h-18z" fill="#fff"/>
    <rect x="18" y="8" width="8" height="16" fill="#fff"/>
  </svg>

  <section class="tips">
    <p class="tip tip--navy" style="top:361px;height:51px"><span><strong>Bring your own cup</strong> - don’t share cups and food.</span></p>
    <p class="tip tip--green" style="top:469px;height:50px"><span><strong>Elbow tap</strong> instead of handshakes and kisses.</span></p>
    <p class="tip tip--pink" style="top:574px;height:50px"><span><strong>Wash your hands</strong> often - with soap.</span></p>
    <p class="tip tip--teal" style="top:684px;height:82px"><span><strong>Elbow or tissues</strong> when you cough or sneeze,<br>then straight in the bin.</span></p>
    <p class="tip tip--green" style="top:827px;height:83px"><span><strong>Leave your face alone</strong> after touching shared<br>surfaces.</span></p>
    <p class="tip tip--navy" style="top:968px;height:50px"><span><strong>Leave your bugs</strong> at home if you’re feeling unwell.</span></p>
  </section>

  <footer>
    <div class="footer-call"></div>
    <div class="footer-source"></div>
    <p class="call-text">Call health line if you have a cough, a high temperature<br>and shortness of breath - <strong>0800 472 9160</strong></p>
    <p class="source-text">Based on recommendations<br>from <strong>IPB</strong> and <strong>DCT</strong></p>
  </footer>
</main>
</body>
</html>
```